Design for schnapps bottle label "Sol Terrado"

Hi! On a small land lot we are producing our own Italian schnapps "Grappa". For the bottles we would like to modernize our current labes that you find below. The two cats looking at each other should remain, but updated and more modern. I am very much looking forward to your suggestions. Best, Joel

Target Market(s)

Schnapps bottle label

Requirements
Must have
• Cats should resemble the cats that are decorating the house entry (see attached), however, should have a more modern appearance.

Text elements should remain: "Grappa", "Sol Terrado", "Legnoso", "[Vintage Year], "Raccolta No", "Vol %"
Should not have
• Current ornament can be used, replaced or deleted (whatever looks best)

```html
<!DOCTYPE html>
<html lang="en">
<head>
<meta charset="utf-8">
<title>Sol Terrado Grappa Label</title>
<link rel="stylesheet" href="https://fonts.googleapis.com/css2?family=Playfair+Display:wght@400;500&family=Pinyon+Script&display=swap">
<style>
  :root {
    --amber-light: #f9b845;
    --amber-mid: #f4a12a;
    --amber-deep: #ec8a12;
    --ink: #1b1208;
    --cat-top: #2a1a0a;
    --cat-bottom: #120b04;
  }
  * { margin: 0; padding: 0; box-sizing: border-box; }
  html, body { width: 838px; height: 1200px; overflow: hidden; }
  body {
    background: linear-gradient(90deg, var(--amber-deep) 0%, var(--amber-light) 45%, var(--amber-mid) 70%, var(--amber-deep) 100%);
    color: var(--ink);
    font-family: "Playfair Display", Georgia, serif;
    position: relative;
  }
  .label { position: absolute; inset: 0; }
  .title-arc { position: absolute; left: 219px; top: 170px; width: 400px; height: 110px; }
  .title-arc text { font-family: "Playfair Display", Georgia, serif; font-size: 54px; fill: var(--ink); letter-spacing: 2px; }
  .cats-art {
    position: absolute; left: 291px; top: 300px; width: 256px; height: 115px;
    background: linear-gradient(180deg, var(--cat-top), var(--cat-bottom));
    border-radius: 50px 50px 6px 6px;
  }
  .brand-script {
    position: absolute; left: 419px; top: 715px;
    transform: translate(-50%, -50%) rotate(-78deg);
    font-family: "Pinyon Script", cursive;
    font-size: 88px; white-space: nowrap; line-height: 1;
  }
  .details { position: absolute; left: 0; right: 0; top: 968px; text-align: center; }
  .details .edition { font-size: 30px; margin-bottom: 8px; }
  .details .batch, .details .strength { font-size: 21px; line-height: 1.4; }
</style>
</head>
<body>
  <main class="label">
    <svg class="title-arc" viewBox="0 0 400 110" aria-label="Grappa">
      <defs><path id="arc" d="M 40 100 Q 200 45 360 100"/></defs>
      <text text-anchor="middle"><textPath href="#arc" startOffset="50%">GRAPPA</textPath></text>
    </svg>
    <div class="cats-art" role="img" aria-label="Illustration of two black cats stretching toward each other, nose to nose"></div>
    <div class="brand-script">Sol Terrado</div>
    <section class="details">
      <p class="edition">Legnoso 2015</p>
      <p class="batch">Raccolta No.01</p>
      <p class="strength">41.0% Vol.</p>
    </section>
  </main>
</body>
</html>
```